I need to rebrand my public user portal for a new/modern look and feel

I want to take my current user web portal and redesign the look of it. I have included 2 samples of my current user portal and would like options to create a new functional look. This main page below will modify based on the tabs on the top left. Any questions please ask.

```html
<!DOCTYPE html>
<html lang="en">
<head>
<meta charset="utf-8">
<title>Northgate Records Dashboard</title>
<link href="https://fonts.googleapis.com/css2?family=Poppins:wght@400;500;600&display=swap" rel="stylesheet">
<style>
:root{
  --backdrop:#e9e8e8;
  --panel:#ffffff;
  --content:#f8f8f9;
  --maroon:#8e2a2c;
  --maroon-soft:#f7eeee;
  --gold:#8a5a22;
  --brown:#7b6140;
  --ink:#2b2b2b;
  --muted:#555;
  --faint:#a7a7a7;
  --grid:#d8d8d8;
  --blue:#1a5fd0;
  --red:#e3262f;
  --green:#0b7a3a;
  --line-blue:#3b7ddd;
  --line-red:#ea3a3a;
}
*{box-sizing:border-box;margin:0;padding:0}
html,body{width:1200px;height:1200px;overflow:hidden;background:var(--backdrop);font-family:'Poppins',sans-serif;color:var(--ink)}
.stage{position:absolute;left:0;top:0;width:1600px;height:1600px;transform:scale(.75);transform-origin:0 0}
.abs{position:absolute}
.panel{left:28px;top:300px;width:1544px;height:998px;background:var(--content)}
.topbar{left:28px;top:300px;width:1544px;height:83px;background:var(--panel);box-shadow:0 3px 6px rgba(0,0,0,.06)}
.brand{left:52px;top:322px;display:flex;align-items:center;gap:10px;font-weight:600;font-size:20px;color:var(--maroon)}
.brand-mark{width:34px;height:34px;border-radius:50%;background:var(--maroon)}
.search{left:215px;top:323px;width:215px;height:37px;border:1px solid #ddd;border-radius:4px;font-size:10px;color:#ccc;padding:10px 0 0 38px}
.search svg{position:absolute;left:8px;top:8px}
.title{left:0;width:1600px;top:326px;text-align:center;font-size:22px;font-weight:600;color:var(--maroon)}
.sidebar{left:28px;top:383px;width:263px;height:915px;background:var(--panel);border-right:1px solid #eee}
.avatar{left:118px;top:447px;width:82px;height:82px;border-radius:50%;background:linear-gradient(#6d5a4c,#3e3530)}
.user-name{left:28px;width:263px;top:538px;text-align:center;font-size:18px;font-weight:600;color:var(--maroon)}
.user-loc{left:28px;width:263px;top:566px;text-align:center;font-size:14px;color:var(--muted)}
.nav-item{left:50px;font-size:18px;color:var(--faint);display:flex;align-items:center;gap:14px}
.nav-item i{display:block;width:20px;height:20px;border-radius:3px;background:#c4c4c4}
.nav-active{left:40px;top:631px;width:229px;height:46px;background:#f6f4f4;box-shadow:0 3px 6px rgba(0,0,0,.12);border-radius:4px;padding:10px 0 0 10px;color:var(--maroon)}
.nav-active i{background:var(--maroon)}
.tab{top:405px;font-size:15px;font-weight:500;display:flex;align-items:center;gap:18px;color:var(--ink)}
.tab-active{left:322px;color:var(--maroon);border-bottom:2px solid var(--maroon);padding-bottom:4px}
.tab i{display:block;width:20px;height:20px;border-radius:3px;background:currentColor}
.greet{left:322px;top:448px;font-size:24px;font-weight:600;line-height:35px;color:var(--maroon)}
.intro{left:322px;top:574px;width:330px;font-size:14px;line-height:22px;color:var(--gold)}
.add-box{left:667px;top:449px;width:218px;height:192px;background:var(--maroon-soft);border:2px dashed var(--maroon);border-radius:14px}
.add-box span{position:absolute;left:96px;top:82px;width:26px;height:26px;background:var(--maroon);border-radius:3px;color:#fff;font-size:22px;line-height:24px;text-align:center}
.card{background:var(--panel);border-radius:16px;box-shadow:0 2px 8px rgba(0,0,0,.07)}
.art{border-radius:8px;background:linear-gradient(135deg,#f2eded,#e4d6d6)}
.btn{background:var(--maroon);color:#fff;font-size:13px;text-align:center;border-radius:3px;line-height:31px;width:107px;height:31px}
.card-title{font-size:22px;font-weight:500}
.card-sub{font-size:13px;color:var(--ink)}
.expand{width:28px;height:28px;border:1.5px solid #333;border-radius:50%;font-size:15px;line-height:24px;text-align:center}
.drop{left:335px;top:771px;width:284px;height:97px;border:2px dashed var(--maroon);border-radius:10px;background:#fbf6f6;text-align:center;font-size:15px;color:var(--maroon);padding-top:52px}
.legend{display:flex;align-items:center;gap:7px;font-size:13px;font-weight:500}
.ficon{display:inline-block;width:16px;height:21px;border-radius:2px}
.f-doc{background:var(--blue)}.f-pdf{background:var(--red)}.f-xls{background:var(--green)}
.doc-row{left:689px;width:339px;height:46px;border:1.5px solid var(--maroon);border-radius:4px;display:flex;align-items:center;padding-left:12px;gap:10px;font-size:15px}
.doc-row .btn{position:absolute;right:6px;top:6px;width:74px;height:32px;line-height:32px;font-size:14px}
.stat{left:697px;font-size:16px;display:flex;align-items:center;gap:8px;border-bottom:2px solid #ccc;padding-bottom:2px;width:92px}
.stat::after{content:"";position:absolute;left:0;bottom:-2px;width:34px;height:2px;background:var(--maroon)}
.flag{width:26px;height:18px;border-radius:2px}
.map{left:806px;top:1092px;width:232px;height:130px;border-radius:50px;background:linear-gradient(120deg,#e8e8ea,#d9d9dc)}
.period{font-size:13px}
.period-active{border:1.5px solid var(--maroon);color:var(--maroon);border-radius:3px;padding:3px 14px}
.dot{width:16px;height:16px;border-radius:50%;display:inline-block}
.charts{left:0;top:0}
.charts text{font-family:'Poppins',sans-serif;font-size:10px;fill:#666}
.charts .donut-label{font-size:17px;font-weight:600}
</style>
</head>
<body>
<div class="stage">
  <div class="abs panel"></div>
  <div class="abs sidebar"></div>
  <header class="abs topbar"></header>
  <div class="abs brand"><span class="brand-mark"></span>Northgate</div>
  <div class="abs search"><svg width="22" height="22" viewBox="0 0 22 22"><circle cx="9" cy="9" r="7" fill="none" stroke="#bbb" stroke-width="2"/><line x1="14" y1="14" x2="20" y2="20" stroke="#bbb" stroke-width="2"/></svg>Search</div>
  <h1 class="abs title">Northgate Records Dashboard</h1>
  <svg class="abs" style="left:1480px;top:332px" width="66" height="22" viewBox="0 0 66 22"><circle cx="11" cy="11" r="8" fill="none" stroke="#bbb" stroke-width="2"/><path d="M49 18h18M51 17c0-9 2-13 7-13s7 4 7 13z" fill="#bbb"/></svg>

  <!-- sidebar -->
  <div class="abs avatar" role="img" aria-label="User profile photo"></div>
  <div class="abs user-name">Daniel Morrow</div>
  <div class="abs user-loc">Denver, USA</div>
  <div class="abs nav-item nav-active"><i></i>Dashboard</div>
  <div class="abs nav-item" style="top:711px"><i></i>Manage Document</div>
  <div class="abs nav-item" style="top:770px"><i></i>Online Hosting</div>
  <div class="abs nav-item" style="top:829px"><i></i>Analytics</div>
  <div class="abs nav-item" style="top:888px"><i></i>Scanning</div>
  <div class="abs nav-item" style="top:948px"><i></i>Shredding</div>

  <!-- tabs & greeting -->
  <div class="abs tab tab-active"><i></i>Dashboard</div>
  <div class="abs tab" style="left:484px"><i style="background:#555"></i>Workflow Automation</div>
  <div class="abs greet">Hi, Daniel!<br>What are your<br>planes for today?</div>
  <p class="abs intro">This platform is designed to revolutionise the way you manage and access your data.</p>
  <div class="abs add-box"><span>+</span></div>

  <div class="abs card" style="left:915px;top:449px;width:296px;height:192px"></div>
  <div class="abs art" style="left:1005px;top:458px;width:120px;height:90px" role="img" aria-label="Illustration of a person beside locked documents"></div>
  <div class="abs" style="left:915px;top:562px;width:296px;text-align:center;font-size:18px;font-weight:500">Secure Docs Storage</div>
  <div class="abs btn" style="left:1010px;top:599px">Learn More</div>

  <div class="abs card" style="left:1240px;top:449px;width:296px;height:192px"></div>
  <div class="abs art" style="left:1325px;top:455px;width:125px;height:92px" role="img" aria-label="Illustration of a person converting a document"></div>
  <div class="abs" style="left:1240px;top:562px;width:296px;text-align:center;font-size:18px;font-weight:500">Convert Documents</div>
  <div class="abs btn" style="left:1335px;top:599px">Learn More</div>

  <!-- upload -->
  <div class="abs card" style="left:322px;top:677px;width:317px;height:215px"></div>
  <div class="abs card-title" style="left:339px;top:688px">Upload Documents</div>
  <div class="abs card-sub" style="left:339px;top:724px">You can upload your documents to store.</div>
  <div class="abs expand" style="left:600px;top:688px">↗</div>
  <div class="abs drop">Drop your file here or browse</div>
  <svg class="abs" style="left:467px;top:795px" width="20" height="20" viewBox="0 0 20 20"><path d="M10 14V3M6 7l4-4 4 4M3 12v5h14v-5" fill="none" stroke="#333" stroke-width="1.6"/></svg>

  <!-- performance -->
  <div class="abs card" style="left:322px;top:918px;width:317px;height:363px"></div>
  <div class="abs card-title" style="left:338px;top:932px">Performance Metrics</div>
  <div class="abs card-sub" style="left:338px;top:964px">Check no.of time you have access your data.</div>
  <div class="abs expand" style="left:600px;top:929px">↗</div>
  <div class="abs legend" style="left:356px;top:997px"><span class="ficon f-doc"></span>Documents&nbsp;&nbsp;<span class="ficon f-pdf"></span>PDF&nbsp;&nbsp;<span class="ficon f-xls"></span>Excel</div>

  <!-- recent -->
  <div class="abs card" style="left:680px;top:677px;width:358px;height:263px"></div>
  <div class="abs card-title" style="left:697px;top:688px">Recent Viewed/Modify</div>
  <div class="abs card-sub" style="left:697px;top:724px">Check view and modified documents.</div>
  <div class="abs expand" style="left:1001px;top:688px">↗</div>
  <div class="abs doc-row" style="top:751px"><span class="ficon f-doc"></span>Statistics of workflow.docs<span class="btn">Viewed</span></div>
  <div class="abs doc-row" style="top:815px"><span class="ficon f-pdf"></span>Statistics of workflow.pdf<span class="btn">Viewed</span></div>
  <div class="abs doc-row" style="top:879px"><span class="ficon f-xls"></span>Statistics of workflow.excel<span class="btn">Modified</span></div>

  <!-- active users -->
  <div class="abs card" style="left:680px;top:967px;width:358px;height:314px"></div>
  <div class="abs card-title" style="left:697px;top:980px">Active Users</div>
  <div class="abs card-sub" style="left:697px;top:1012px">Number of user using Northgate Records</div>
  <div class="abs expand" style="left:996px;top:982px">↗</div>
  <div class="abs" style="left:697px;top:1043px;font-size:22px;font-weight:500">10.8k</div>
  <div class="abs stat" style="top:1096px"><span class="flag" style="background:linear-gradient(#f29a33 33%,#fff 33% 66%,#1e8a3a 66%)"></span>IN <small>27%</small></div>
  <div class="abs stat" style="top:1160px"><span class="flag" style="background:repeating-linear-gradient(#c8102e 0 2.6px,#fff 2.6px 5.2px)"></span>US <small>48%</small></div>
  <div class="abs stat" style="top:1225px"><span class="flag" style="background:#1f3f8f"></span>US <small>25%</small></div>
  <div class="abs map" role="img" aria-label="World map highlighting user regions"></div>

  <!-- overview -->
  <div class="abs card" style="left:1086px;top:677px;width:450px;height:374px"></div>
  <div class="abs card-title" style="left:1104px;top:692px">Overview</div>
  <div class="abs period" style="left:1237px;top:700px">Week</div>
  <div class="abs period period-active" style="left:1294px;top:695px">Month</div>
  <div class="abs period" style="left:1388px;top:700px">Year</div>
  <div class="abs expand" style="left:1496px;top:688px">↗</div>
  <div class="abs legend" style="left:1187px;top:1022px;color:#888;font-weight:400"><span class="dot" style="background:var(--maroon)"></span>Accessed</div>
  <div class="abs legend" style="left:1324px;top:1022px;color:#888;font-weight:400"><span class="dot" style="background:var(--brown)"></span>Edits / Modify</div>

  <!-- expense -->
  <div class="abs card" style="left:1086px;top:1066px;width:450px;height:205px"></div>
  <div class="abs card-title" style="left:1104px;top:1076px">Expense Tracking</div>
  <div class="abs legend" style="left:1305px;top:1084px;font-weight:400"><span class="dot" style="background:var(--line-blue)"></span>Earnings</div>
  <div class="abs legend" style="left:1398px;top:1084px;font-weight:400"><span class="dot" style="background:var(--line-red)"></span>Expense</div>
  <div class="abs expand" style="left:1496px;top:1073px">↗</div>

  <svg class="abs charts" width="1600" height="1600" viewBox="0 0 1600 1600">
    <!-- donut -->
    <g fill="none" stroke-width="24">
      <path d="M476 1227 A78 78 0 0 1 476 1071" stroke="var(--red)"/>
      <path d="M484 1071 A78 78 0 0 1 554 1143" stroke="var(--blue)"/>
      <path d="M554 1155 A78 78 0 0 1 484 1227" stroke="var(--green)"/>
    </g>
    <text x="476" y="1156" text-anchor="middle" style="font-size:21px;fill:#222;font-weight:500">100%</text>
    <text class="donut-label" x="336" y="1162" style="fill:var(--red)">50%</text>
    <text class="donut-label" x="548" y="1087" style="fill:var(--blue)">25%</text>
    <text class="donut-label" x="546" y="1231" style="fill:var(--green)">25%</text>

    <!-- overview grid -->
    <g stroke="var(--grid)" stroke-dasharray="3 3">
      <line x1="1133" y1="751" x2="1515" y2="751"/><line x1="1133" y1="797" x2="1515" y2="797"/>
      <line x1="1133" y1="843" x2="1515" y2="843"/><line x1="1133" y1="888" x2="1515" y2="888"/>
      <line x1="1133" y1="934" x2="1515" y2="934"/><line x1="1133" y1="980" x2="1515" y2="980"/>
    </g>
    <g text-anchor="end"><text x="1124" y="755">250</text><text x="1124" y="801">200</text><text x="1124" y="847">150</text><text x="1124" y="892">100</text><text x="1124" y="938">50</text><text x="1124" y="984">0</text></g>
    <g text-anchor="middle">
      <text x="1154" y="743">Jan</text><text x="1196" y="743">Feb</text><text x="1238" y="743">Mar</text><text x="1281" y="743">April</text><text x="1323" y="743">June</text><text x="1366" y="743">July</text><text x="1408" y="743">Aug</text><text x="1450" y="743">Sept</text><text x="1493" y="743">Oct</text>
      <text x="1154" y="996">Jan</text><text x="1196" y="996">Feb</text><text x="1238" y="996">Mar</text><text x="1281" y="996">April</text><text x="1323" y="996">June</text><text x="1366" y="996">July</text><text x="1408" y="996">Aug</text><text x="1450" y="996">Sept</text><text x="1493" y="996">Oct</text>
    </g>
    <path d="M1155 976 C1200 973 1240 972 1265 965 C1290 958 1300 945 1320 935 C1345 925 1355 935 1368 905 C1385 860 1390 770 1408 768 C1425 766 1425 930 1445 936 C1460 940 1480 932 1493 932" fill="none" stroke="var(--maroon)" stroke-width="1.6"/>
    <path d="M1240 970 C1265 962 1280 955 1300 955 C1330 952 1355 940 1370 905 C1385 860 1390 820 1410 815 C1430 812 1455 812 1465 815 C1480 825 1490 880 1493 932" fill="none" stroke="var(--brown)" stroke-width="1.6"/>

    <!-- expense grid -->
    <g stroke="var(--grid)" stroke-dasharray="3 3">
      <line x1="1133" y1="1127" x2="1518" y2="1127"/><line x1="1133" y1="1155" x2="1518" y2="1155"/>
      <line x1="1133" y1="1183" x2="1518" y2="1183"/><line x1="1133" y1="1211" x2="1518" y2="1211"/>
      <line x1="1133" y1="1239" x2="1518" y2="1239"/>
    </g>
    <g text-anchor="end"><text x="1124" y="1131">200</text><text x="1124" y="1159">150</text><text x="1124" y="1187">100</text><text x="1124" y="1215">50</text><text x="1124" y="1243">0</text></g>
    <g text-anchor="middle"><text x="1160" y="1250">Mon</text><text x="1215" y="1250">Tue</text><text x="1270" y="1250">Wed</text><text x="1325" y="1250">Thrus</text><text x="1380" y="1250">Fri</text><text x="1435" y="1250">Sat</text><text x="1490" y="1250">Sun</text></g>
    <polyline points="1160,1170 1215,1132 1270,1160 1325,1205 1380,1170 1435,1185 1490,1213" fill="none" stroke="var(--line-blue)" stroke-width="2"/>
    <polyline points="1160,1183 1215,1222 1270,1155 1325,1170 1380,1127 1435,1212 1490,1152" fill="none" stroke="var(--line-red)" stroke-width="2"/>
  </svg>
</div>
</body>
</html>
```